Commercial Bakery needs packing design for a Bread Bag.

Brenton's Bakery needs a design for a bread bag to be distributed to grocery stores. We make all kinds of breads and want this packaging to represent our company. We would like the packaging to be black and white with a fun/bubbly modern design. I have attached a few ideas of what I am looking for.
There are 5 different products. Packaging must be the same for each product except for corresponding product name, bar code and nutrional facts.
Product names:
Coconut Cream Bread
Cream Bread
Potato Rolls
Roll ups
Coconut & Raisin Bread

Our products are packaged in a 11” x 8” poly bag.
I will open 5 contracts with whoever’s design I select. I will then provide nutritional facts, barcodes for items once a contract is selected. Thank you!!

Target Market(s)

Grocery stores

Industry/Entity Type

Bakery

Requirements
Must have
• Black and White (off whites are ok)
Should not have
• Color

```html
<!DOCTYPE html>
<html lang="en">
<head>
<meta charset="utf-8">
<title>Brenton's Bakery – Coconut Cream Bread Bag</title>
<link rel="stylesheet" href="https://fonts.googleapis.com/css2?family=Kalam:wght@700&family=Roboto+Condensed:wght@400;700&display=swap">
<style>
  :root {
    --backdrop: #f2f2f2;
    --bag-black: #111111;
    --band-white: #f4f4f4;
    --band-edge: #b9b9b9;
    --silver: #d9d9d9;
    --ink-dark: #2b2b2b;
    --muted: #8a8a8a;
    --white: #ffffff;
  }
  * { box-sizing: border-box; margin: 0; padding: 0; }
  html, body { width: 1200px; height: 1200px; overflow: hidden; }
  body { background: var(--backdrop); position: relative; font-family: "Roboto Condensed", Arial, sans-serif; }

  .bag-front {
    position: absolute; left: 380px; top: 190px;
    width: 440px; height: 820px;
    background: var(--bag-black);
    border-radius: 10px;
    overflow: hidden;
  }
  .band-art { position: absolute; inset: 0; width: 440px; height: 820px; }

  .tagline {
    position: absolute; top: 30px; left: 0; width: 100%;
    text-align: center; color: var(--white);
    font-family: "Kalam", "Comic Sans MS", cursive;
    font-weight: 700; font-size: 34px; letter-spacing: 0.5px;
    transform: rotate(-3deg);
  }

  .brand-seal {
    position: absolute; left: 73px; top: 178px;
    width: 266px; height: 266px;
    border: 3px solid var(--ink-dark); border-radius: 50%;
    display: flex; flex-direction: column; align-items: center; justify-content: center;
    color: var(--ink-dark); font-family: "Roboto Condensed", Arial, sans-serif; font-weight: 700;
  }
  .brand-name { font-size: 44px; line-height: 1; }
  .brand-sub { font-size: 18px; letter-spacing: 3px; margin-top: 8px; }

  .wheat-crest {
    position: absolute; left: 237px; top: 118px; width: 70px; height: 140px;
    background: linear-gradient(160deg, #4a4a4a, #1e1e1e);
    border-radius: 40% 40% 20% 20%;
  }

  .product-name {
    position: absolute; top: 520px; left: 0; width: 100%;
    text-align: center; color: var(--silver); font-weight: 700; text-transform: uppercase;
  }
  .product-name .line-small { display: block; font-size: 32px; line-height: 1.1; }
  .product-name .line-large { display: block; font-size: 44px; line-height: 1.05; }

  .range-box {
    position: absolute; left: 40px; top: 641px; width: 172px; height: 115px;
    border: 1.5px solid #5a5a5a; border-radius: 6px;
    padding: 26px 10px 8px 12px; color: var(--silver);
  }
  .range-title {
    position: absolute; left: -12px; top: 12px;
    background: linear-gradient(90deg, #e8e8e8, #a9a9a9);
    color: var(--bag-black); font-size: 9px; font-weight: 700;
    padding: 2px 8px; white-space: nowrap;
  }
  .range-list { list-style: none; margin-top: 14px; font-size: 10.5px; line-height: 1.45; }
  .range-list li::before { content: "• "; }

  .net-weight {
    position: absolute; left: 200px; top: 760px; width: 50px; height: 50px;
    border-radius: 50%; background: var(--white); color: var(--bag-black);
    font-size: 11px; font-weight: 700;
    display: flex; align-items: center; justify-content: center;
  }

  .wheat-sprig {
    position: absolute; left: 290px; top: 648px; width: 112px; height: 172px;
    background: linear-gradient(170deg, #f0f0f0, #9a9a9a);
    border-radius: 45% 45% 10% 10%;
  }
</style>
</head>
<body>
  <main class="bag-front">
    <svg class="band-art" viewBox="0 0 440 820" role="img" aria-label="Off-white band with a light line-drawn pattern of breads, croissants and pastries">
      <polygon points="0,120 440,70 440,457 0,515" fill="var(--band-white)"/>
      <line x1="0" y1="120" x2="440" y2="70" stroke="var(--band-edge)" stroke-width="5"/>
      <line x1="0" y1="515" x2="440" y2="457" stroke="var(--band-edge)" stroke-width="5"/>
    </svg>

    <p class="tagline">Fresh and natural</p>

    <div class="brand-seal">
      <span class="brand-name">Brenton's</span>
      <span class="brand-sub">BAKERY &amp; CAFÉ</span>
    </div>
    <div class="wheat-crest" role="img" aria-label="Illustration of three wheat ears"></div>

    <h1 class="product-name">
      <span class="line-small">Coconut Cream</span>
      <span class="line-large">Bread</span>
    </h1>

    <section class="range-box">
      <span class="range-title">DISCOVER OUR OTHER BREADS</span>
      <ul class="range-list">
        <li>CREAM BREAD</li>
        <li>POTATO ROLLS</li>
        <li>ROLL UPS</li>
        <li>COCONUT &amp; RAISIN BREAD</li>
      </ul>
    </section>

    <div class="net-weight">250 gms</div>

    <div class="wheat-sprig" role="img" aria-label="White illustration of wheat stalks"></div>
  </main>
</body>
</html>
```